Voren Spark Services requires a modern & sharp looking sign.

We need a sign to be designed for a local soccer club ground where advertising will take place. Text needs to be limited with only the basic information such as the logo/company name, website and mobile number. The EC40293 number must be placed somewhere in the sign.

The design should be similar to the flyer design attached, but in a more plain looking version.

Signage dimensions are 2050mm Wide x 900mm High.

Industry/Entity Type

Electrician

Requirements
Must have
• Logo/Company Name
• EC Number
• Website (www.vorenspark.com.au)
• Phone Number
• - SAME COLOR SCHEME AS THE LOGO
• - SAME LIGHTNING BOLT TO THE RIGHT OF THE SIGN (REFER TO FLYER)
Should not have
• NO PICTURES

```html
<!DOCTYPE html>
<html lang="en">
<head>
<meta charset="utf-8">
<title>Voren Spark Services – Ground Sign</title>
<link rel="stylesheet" href="https://fonts.googleapis.com/css2?family=Open+Sans:wght@400;600;700&display=swap">
<style>
  :root {
    --brand-blue: #2b4fa3;
    --brand-blue-soft: #6d86c4;
    --sky-blue: #2f7fc9;
    --steel-grey: #67686b;
    --ink: #1b1b1b;
    --silver-dark: #c4c5c8;
    --silver-mid: #d9dadc;
    --silver-light: #ececed;
    --white: #ffffff;
  }
  * { box-sizing: border-box; margin: 0; padding: 0; }
  html, body { width: 1200px; height: 527px; overflow: hidden; background: var(--silver-mid); }
  .sign {
    position: relative;
    width: 1200px;
    height: 527px;
    overflow: hidden;
    font-family: "Open Sans", Arial, sans-serif;
    background:
      linear-gradient(115deg, transparent 0 40%, rgba(255,255,255,.35) 52%, transparent 64%),
      linear-gradient(160deg, var(--silver-dark) 0%, var(--silver-mid) 45%, var(--silver-light) 100%);
  }

  .brand {
    position: absolute;
    left: 40px;
    top: 22px;
    display: flex;
    align-items: center;
    gap: 18px;
  }
  .brand-dot {
    width: 112px;
    height: 112px;
    border-radius: 50%;
    background: var(--brand-blue);
    flex: none;
  }
  .brand-name {
    color: var(--brand-blue);
    font-weight: 700;
    line-height: 1;
  }
  .brand-name .line-main { display: block; font-size: 62px; letter-spacing: 1px; }
  .brand-name .line-sub { display: block; font-size: 32px; letter-spacing: 8px; margin-top: 10px; }

  .tagline {
    position: absolute;
    left: 54px;
    top: 180px;
    font-weight: 400;
    line-height: 1.05;
    color: var(--sky-blue);
    font-size: 43px;
  }
  .tagline .accent { color: var(--steel-grey); font-weight: 700; }

  .contacts {
    position: absolute;
    left: 48px;
    top: 314px;
    list-style: none;
  }
  .contact {
    display: flex;
    align-items: center;
    color: var(--brand-blue);
    white-space: nowrap;
  }
  .contact-icon { width: 38px; height: 38px; flex: none; margin-right: 22px; }
  .contact-phone { font-size: 51px; font-weight: 700; letter-spacing: 1px; height: 60px; }
  .contact-email { font-size: 44px; font-weight: 400; height: 50px; }
  .contact-web { font-size: 43px; font-weight: 400; height: 50px; }

  .licence {
    position: absolute;
    left: 274px;
    top: 487px;
    color: var(--brand-blue);
    font-weight: 700;
    font-size: 22px;
    letter-spacing: 1px;
  }

  .emblem-area {
    position: absolute;
    left: 614px;
    top: -26px;
    width: 580px;
    height: 580px;
  }
</style>
</head>
<body>
<main class="sign">
  <header class="brand">
    <span class="brand-dot"></span>
    <h1 class="brand-name">
      <span class="line-main">VOREN SPARK</span>
      <span class="line-sub">SERVICES</span>
    </h1>
  </header>

  <p class="tagline">
    YOUR <span class="accent">TRUSTED</span><br>
    ELECTRICAL CONTRACTOR
  </p>

  <ul class="contacts">
    <li class="contact contact-phone">
      <svg class="contact-icon" viewBox="0 0 38 38" aria-hidden="true">
        <circle cx="19" cy="19" r="16" fill="none" stroke="var(--ink)" stroke-width="2"/>
        <path d="M14 10 q-3 9 3 18 l3 -2 -3 -5 -2 1 q-2 -5 0 -10 l2 1 2 -5 z" fill="var(--ink)"/>
      </svg>
      0491 570 318
    </li>
    <li class="contact contact-email">
      <svg class="contact-icon" viewBox="0 0 38 38" aria-hidden="true">
        <rect x="5" y="10" width="28" height="19" fill="none" stroke="var(--ink)" stroke-width="2"/>
        <path d="M5 10 L19 22 L33 10 M5 29 L15 19 M33 29 L23 19" fill="none" stroke="var(--ink)" stroke-width="2"/>
      </svg>
      dario@vorenspark.com
    </li>
    <li class="contact contact-web">
      <svg class="contact-icon" viewBox="0 0 38 38" aria-hidden="true">
        <circle cx="23" cy="17" r="11" fill="none" stroke="var(--ink)" stroke-width="2"/>
        <path d="M12 17 H34 M23 6 V28 M23 6 q-7 11 0 22 M23 6 q7 11 0 22" fill="none" stroke="var(--ink)" stroke-width="1.5"/>
        <path d="M15 25 L4 34" stroke="var(--ink)" stroke-width="4" stroke-linecap="round"/>
      </svg>
      www.vorenspark.com.au
    </li>
  </ul>

  <p class="licence">EC40293</p>

  <svg class="emblem-area" viewBox="0 0 580 580" role="img" aria-label="Large brand emblem decoration in blue, white and silver">
    <defs>
      <linearGradient id="emblem-tones" x1="0" y1="0" x2="1" y2="1">
        <stop offset="0%" stop-color="#c9cacd"/>
        <stop offset="22%" stop-color="#f4f5f7"/>
        <stop offset="48%" stop-color="#b9c6e4"/>
        <stop offset="72%" stop-color="#2b4fa3"/>
        <stop offset="100%" stop-color="#24448f"/>
      </linearGradient>
    </defs>
    <circle cx="290" cy="316" r="290" fill="url(#emblem-tones)"/>
  </svg>
</main>
</body>
</html>
```